VENTURE CAPITAL GROUP BUSINESS CARD DESIGN

Venture Capital Group based in SF looking for a bold business card design. No trendy colour explosion, 3D effects etc. Just "simple" optical effects. Works on your brain, keeps your eye focused and sticks to your mind.
Target Market(s)
Technology startups
Industry/Entity Type
Venture Capital
Contact Information for Business Card
BARNABY WHITLOCK
MANAGING PARTNER
817 FERN ST SAN FRANCISCO, CA 94111
415.555.0143 O
415.555.0167 F
415.555.0192 C
barn@halcyonridgefund.example

```html
<!DOCTYPE html>
<html lang="en">
<head>
<meta charset="utf-8">
<title>Halcyon Ridge Business Card</title>
<link href="https://fonts.googleapis.com/css2?family=Arimo:wght@400&display=swap" rel="stylesheet">
<style>
  :root {
    --backdrop: #a6d57a;
    --card-grey: #6f8387;
    --band-green: #056b08;
    --band-black: #000000;
    --ink-green: #0b4a12;
    --ink-muted: #8ea2a6;
    --rule: #4f6a52;
    --ring: #7a8f93;
  }
  * { margin: 0; padding: 0; box-sizing: border-box; }
  html, body {
    width: 1200px; height: 1200px; overflow: hidden;
    background: var(--backdrop);
    font-family: "Arimo", Arial, sans-serif;
  }
  .card {
    position: absolute; left: 182px; width: 840px; height: 480px;
    background: var(--card-grey); overflow: hidden;
  }
  .card--front { top: 98px; }
  .card--back { top: 640px; }
  .band { position: absolute; left: 0; width: 100%; }
  .band--green { background: var(--band-green); }
  .band--black { background: var(--band-black); bottom: 0; height: 44px; }
  .mark-circle {
    position: absolute; width: 160px; height: 160px; border-radius: 50%;
    left: 341px; background: var(--ring); opacity: 0.55;
  }
  .brand-name {
    position: absolute; left: 0; width: 100%; text-align: center;
    font-size: 44px; letter-spacing: 3px; color: var(--ink-green);
    text-transform: uppercase; line-height: 1;
  }
  .divider {
    position: absolute; left: 0; width: 100%; top: 274px; height: 2px;
    background: var(--rule);
  }
  .person {
    position: absolute; left: 0; width: 100%; text-align: center;
    color: var(--ink-muted);
  }
  .person__name { top: 287px; font-size: 21px; }
  .person__title { top: 315px; font-size: 17px; }
  .phones {
    position: absolute; top: 367px; left: 0; width: 100%;
    display: flex; justify-content: center; gap: 42px;
    font-size: 18px; color: var(--ink-muted);
  }
  .contact-line {
    position: absolute; top: 402px; left: 48px; right: 48px;
    display: flex; justify-content: space-between;
    font-size: 18px; color: var(--ink-muted);
  }
  .contact-item { display: flex; align-items: center; gap: 8px; }
  .contact-item svg { flex: none; }
</style>
</head>
<body>

<section class="card card--front">
  <div class="band band--green" style="top:0;height:13px"></div>
  <div class="band band--green" style="top:238px;height:198px"></div>
  <div class="divider"></div>
  <div class="band band--black"></div>

  <div class="mark-circle" style="top:26px"></div>
  <div class="brand-name" style="top:196px">Halcyon Ridge</div>

  <div class="person person__name">Barnaby Whitlock</div>
  <div class="person person__title">Managing Partner</div>

  <div class="phones">
    <span>[O]&nbsp; 415.555.0143</span>
    <span>[F]&nbsp; 415.555.0167</span>
    <span>[C]&nbsp; 415.555.0192</span>
  </div>

  <div class="contact-line">
    <span class="contact-item">
      <svg width="18" height="18" viewBox="0 0 18 18" aria-hidden="true">
        <circle cx="9" cy="9" r="8" fill="none" stroke="#8ea2a6" stroke-width="1.6"/>
        <path d="M1 9h16M9 1c-3 3-3 13 0 16M9 1c3 3 3 13 0 16" fill="none" stroke="#8ea2a6" stroke-width="1.2"/>
      </svg>
      barn@halcyonridgefund.example
    </span>
    <span class="contact-item">
      <svg width="14" height="20" viewBox="0 0 14 20" aria-hidden="true">
        <path d="M7 0C3 0 0 3 0 7c0 5 7 13 7 13s7-8 7-13c0-4-3-7-7-7z" fill="#8ea2a6"/>
        <circle cx="7" cy="7" r="2.6" fill="#056b08"/>
      </svg>
      817 Fern St. San Francisco, CA 94111
    </span>
  </div>
</section>

<section class="card card--back">
  <div class="band band--green" style="top:0;height:24px"></div>
  <div class="band band--black"></div>

  <div class="mark-circle" style="top:92px"></div>
  <div class="brand-name" style="top:272px">Halcyon Ridge</div>
</section>

</body>
</html>
```